Veltarum

Standard Business Card design.
Sample two-sided design uploaded. White front, Black back.
Would like white shield to be on all black background side.
Willing to look at a couple creative designs, but nothing crazy.
Preference for a classic, confident, strong design.

```html
<!DOCTYPE html>
<html lang="en">
<head>
<meta charset="utf-8">
<title>Veltarum Business Card Presentation</title>
<link href="https://fonts.googleapis.com/css2?family=Fira+Sans+Condensed:wght@400;600&family=Source+Code+Pro:wght@400&display=swap" rel="stylesheet">
<style>
  :root {
    --sheet: #ffffff;
    --ink: #0a0a0b;
    --card-black: #000000;
    --card-border: #c8c8c8;
    --silver: #b4b4b4;
    --silver-light: #ededed;
    --silver-dark: #8c8c8c;
    --text-light: #f2f2f2;
    --caption: #111111;
  }
  * { margin: 0; padding: 0; box-sizing: border-box; }
  html, body {
    width: 1200px;
    height: 796px;
    overflow: hidden;
    background: var(--sheet);
  }
  .sheet {
    position: relative;
    width: 1200px;
    height: 796px;
    overflow: hidden;
    background: var(--sheet);
    font-family: "Fira Sans Condensed", "Arial Narrow", sans-serif;
  }
  .card {
    position: absolute;
    top: 46px;
    width: 467px;
    height: 302px;
  }
  .card--front {
    left: 107px;
    background: var(--sheet);
    border: 1px solid var(--card-border);
    display: flex;
    align-items: center;
    justify-content: center;
  }
  .card--front .brand-name {
    font-size: 64px;
    font-weight: 600;
    letter-spacing: 6px;
    color: var(--ink);
    text-transform: uppercase;
  }
  .card--back {
    left: 586px;
    background: var(--card-black);
    color: var(--text-light);
    text-align: center;
  }
  .card--back .brand {
    position: absolute;
    top: 32px;
    left: 0;
    right: 0;
    display: flex;
    align-items: center;
    justify-content: center;
    gap: 14px;
  }
  .brand-mark {
    width: 30px;
    height: 30px;
    border-radius: 50%;
    background: var(--text-light);
  }
  .card--back .brand-name {
    font-size: 30px;
    font-weight: 600;
    letter-spacing: 4px;
    text-transform: uppercase;
    color: var(--text-light);
  }
  .holder {
    position: absolute;
    top: 146px;
    left: 0;
    right: 0;
  }
  .holder-name {
    font-size: 22px;
    font-weight: 600;
    color: var(--silver);
    line-height: 1.1;
  }
  .holder-role {
    font-size: 17px;
    font-weight: 400;
    color: var(--text-light);
    line-height: 1.3;
  }
  .contact {
    position: absolute;
    top: 265px;
    left: 0;
    right: 0;
    font-size: 15px;
    font-weight: 400;
    color: var(--text-light);
    white-space: nowrap;
  }
  .foil-name {
    position: absolute;
    top: 499px;
    left: 0;
    width: 1160px;
    text-align: center;
    font-size: 35px;
    font-weight: 600;
    line-height: 1;
    background: linear-gradient(180deg, var(--silver-dark) 0%, var(--silver-light) 45%, var(--silver) 60%, var(--silver-light) 100%);
    -webkit-background-clip: text;
    background-clip: text;
    color: transparent;
  }
  .caption {
    position: absolute;
    top: 547px;
    left: 104px;
    width: 950px;
    font-family: "Source Code Pro", monospace;
    font-size: 15px;
    letter-spacing: 1.45px;
    line-height: 1;
    color: var(--caption);
    white-space: nowrap;
  }
  .foil-sample {
    position: absolute;
    top: 590px;
    left: 459px;
    width: 234px;
    height: 158px;
    background: linear-gradient(135deg, #2a2a2a 0%, #3e3e3e 45%, #4a4a4a 70%, #333333 100%);
  }
</style>
</head>
<body>
  <main class="sheet">
    <section class="card card--front">
      <span class="brand-name">Veltarum</span>
    </section>

    <section class="card card--back">
      <div class="brand">
        <span class="brand-mark"></span>
        <span class="brand-name">Veltarum</span>
      </div>
      <div class="holder">
        <p class="holder-name">Name Surname</p>
        <p class="holder-role">Executive Director</p>
      </div>
      <p class="contact">T. 1234 567 7890,&nbsp; hello@veltarum.com,&nbsp; www.veltarum.com</p>
    </section>

    <p class="foil-name">Name Surname</p>
    <p class="caption">The idea is that the name will be printed in silver foil and/or embossed like sample below</p>

    <div class="foil-sample" role="img" aria-label="Photo of dark card stock with a silver hot foil stamped emblem as a finish reference"></div>
  </main>
</body>
</html>
```